Health care finance company startup website design

This design brief is for Ledger Loom, a small start-up company dealing with an online health care (initially dental targeted with plans for medical market) financial suite of tools. My business partners and I are looking to have a website developed for our business model.

We have developed a professional logo and would like it incorporated into the site. We are open to modifications on the logo if needed to accomplish the right design.

Our concept is a clean, simple design with a professional polish and very up-to-date web presence. The functionality of the site is simple yet powerful and we would like it’s design to complement that (including anticipated css3/html5 effects for an added dimension of UI polish).

We would like to see a design mockup of the functional elements of our site as our home page. We would also be very interested to see how your design would flow into the other pages such as search for a loan, create a payment plan, make a payment, sign in, registration, contact us and learn more.

Regarding Functional Elements:

-Simplicity is king.

-The three main functions of the site are the focus. They will operate via a series of API’s to webservices on the back-end, making the front end field focused, though we hope to have it feel friendly and simple.
-Search for a loan
-Create a payment plan
-Make a payment

Other functions of the site include:

-Sign in module
-We plan to support Kindred Link, Vortal Verify and PassGate so incorporating design for those options is a plus.

-Registration module
-Two service levels clients can register for, loans only or loans & payments
-The registration process should be divided into sections with navigation back and forth until a confirmation final screen with pdf generations and remaining “to-do items” listed.
-The registration information will be saved in our database and also auto-populate fields for PDF’s that will be generated from templates.
-The registration will send a confirmation email and support PassGate, Vortal Verify and Kindred Link, so designs should take these programmatic features into account.

-Contact us
-This will emphasize digital forms of communication (email and form submitted contact request).

-Learn more
-Explanations/faqs/tutorials
-This will contain video demonstrations/screencasts of key functions of website features

Regarding Design Elements:
-We want to be “wow’d” and don’t mind a surprise that redefines what we thought we liked regarding design.
-The following examples indicate some of the color schemes we like and design elements we hope to incorporate.
-We also recognize there is no substitute for creativity and originality.

Favorite Website Design Examples:

http://www.joggingwithmarla.example/
HD backgrounds are a plus.
These colors are great.
The bright splashes of blue, red and orange combined with black in these shades.
A predominant background of whitesmoke or beige.

https://tillbrook.example/
The HD backgrounds are sharp.
The look is very clean (though it has a slight Pearfield computers imitation).
The left to right “scrolling” is preferable to vertical scrolling.
Very pleasing to the eye.

http://www.gravelpathworks.example/
Again, use of bright, vibrant HD graphics is exceptional.
The left to right scrolling navigation is slick and likely how we would like our services to flow.

http://buzzing.visitlakeshore.example/
Love the look, feel and concepts in this site’s design
Especially colors and “photography” elements.
Updates

We've seen a few common themes in various designs submitted so far and want to add a few suggestions as we enter the final week of our design contest.

We do not want any photos of healthcare professionals or close-ups of people (families or couples or individuals).  Although we are a health care company we don't want to fall into a cliche feel for our site.  Instead we would like either objects or abstract images that have depth and are high definition, spanning from edge to edge of the width of the screen. 

We prefer shades of grey for the base color scheme with highlights of bright colors.  Please refer to the examples on the brief and use those as the best guide of what we want.  Even SketchHive's color scheme is closer to what we want than some of the submissions, so please take note of the "shades of grey" with splashes of bright accent colors.

We love the horizontal navigation bar like that seen in the gravel-path works site and anticipate our final product using a similar transition between the functions of the site.

Good luck to you all.  We are still looking for that WOW factor and hoping to see something original, that breaks the traditional mold and has a feel like the examples posted.  

Industry/Entity Type

Communication

```html
<!DOCTYPE html>
<html lang="en">
<head>
<meta charset="utf-8">
<title>Ledger Loom</title>
<link href="https://fonts.googleapis.com/css2?family=Arimo:wght@400;700&family=Fredoka:wght@500&family=Lora:ital@1&family=Questrial&family=Tinos&display=swap" rel="stylesheet">
<style>
:root{
  --header-top:#fdfdfd;
  --header-bottom:#dedee2;
  --panel:#eeeeee;
  --line:#c9c9c9;
  --ink:#333333;
  --muted:#777777;
  --brand:#2c3345;
  --green-deep:#2a9446;
  --green-soft:#cfeedb;
  --green-pale:#eef9f2;
  --ribbon:#7fcf6a;
  --ribbon-dark:#4f9a2c;
  --orange:#e08a0e;
  --orange-dark:#d25a00;
  --red:#e8170f;
  --blue:#1a1aea;
  --sky:#2d9be0;
  --footer:#2d2b2c;
  --gold:#e9b22a;
}
*{box-sizing:border-box;margin:0;padding:0}
html,body{width:1158px;height:1200px;overflow:hidden}
body{position:relative;background:var(--green-pale);font-family:'Arimo',sans-serif;color:var(--ink)}
.abs{position:absolute}
.backdrop{left:0;top:147px;width:1158px;height:956px;background:linear-gradient(90deg,var(--green-deep) 0,var(--green-soft) 93px,var(--green-pale) 50%,var(--green-soft) 1061px,var(--green-deep) 100%)}
.header{left:0;top:0;width:1158px;height:147px;background:linear-gradient(var(--header-top),var(--header-bottom))}
.brand{left:43px;top:17px;display:flex;align-items:center;gap:22px}
.brand-mark{width:80px;height:80px;border-radius:10px;background:var(--brand)}
.brand-name{font-family:'Questrial',sans-serif;font-size:54px;color:var(--brand);letter-spacing:1px}
.follow{left:710px;top:37px;width:349px;height:37px;border-radius:8px;background:#e2e2e4;display:flex;align-items:center;font-size:12px;color:#444}
.follow .label{padding:0 14px;border-right:1px solid #c8c8c8;height:100%;display:flex;align-items:center;color:#666}
.follow .item{display:flex;align-items:center;gap:5px;margin-left:14px}
.follow .dot{width:16px;height:16px;border-radius:3px;background:#8a8f99}
.panel{left:93px;top:147px;width:968px;height:919px;background:var(--panel)}
.nav{left:147px;top:107px;width:859px;height:45px;border-radius:10px;background:linear-gradient(#ffffff,#e6e6e6);border:1px solid #cfcfcf;box-shadow:0 6px 8px rgba(0,0,0,.12);z-index:2}
.nav a{position:absolute;top:12px;font-size:17px;color:#666;text-decoration:none}
.nav .sep{position:absolute;top:8px;width:1px;height:28px;background:#cfcfcf}
.hero{left:124px;top:175px;width:900px;height:282px;border:2px solid #c9c9c9;background:radial-gradient(circle at 40% 30%,#fff3c8 0%,var(--gold) 45%,#b87a10 100%)}
.card{top:352px;width:242px;height:210px;border-radius:16px;background:linear-gradient(#ffffff,#e3e3e3);border:1px solid #cfcfcf;box-shadow:0 6px 8px rgba(0,0,0,.12)}
.card .art{position:absolute;left:86px;top:12px;width:70px;height:84px;border-radius:8px}
.card h2{position:absolute;top:112px;width:100%;text-align:center;font-family:'Fredoka',sans-serif;font-weight:500;font-size:22px}
.card p{position:absolute;left:26px;top:146px;width:170px;font-family:'Tinos',serif;font-size:13px;line-height:16px;color:#444}
.btn-more{position:absolute;left:96px;top:172px;width:95px;height:32px;border-radius:6px;background:linear-gradient(#ffffff,#dcdcdc);border:1px solid #c4c4c4;font-size:13px;font-weight:700;color:#555;display:flex;align-items:center;justify-content:center}
.welcome{left:93px;top:588px;width:968px;text-align:center;font-family:'Fredoka',sans-serif;font-weight:500;font-size:22px;color:var(--orange)}
.intro{left:178px;top:640px;width:838px;text-align:center;font-family:'Tinos',serif;font-size:14.5px;line-height:18.5px;color:var(--muted)}
.more-large{left:823px;top:684px;width:119px;height:40px;border-radius:6px;background:repeating-linear-gradient(135deg,#f4f4f4 0 3px,#e4e4e4 3px 5px);border:1px solid #c4c4c4;box-shadow:0 4px 6px rgba(0,0,0,.15);font-size:15px;font-weight:700;color:#555;display:flex;align-items:center;justify-content:center}
.ribbon{left:51px;top:700px;width:288px;height:44px;border-radius:4px;background:linear-gradient(var(--ribbon),var(--ribbon-dark));transform:rotate(3deg)}
.ribbon-text{left:51px;top:700px;width:288px;height:44px;line-height:44px;text-align:center;font-size:19px;font-weight:700;color:#fff;transform:rotate(3deg)}
.login{left:124px;top:751px;width:340px;height:173px;background:#fff;border:1px solid var(--line)}
.login h3{position:absolute;left:22px;top:18px;font-weight:400;font-size:25px;color:#222}
.login label{position:absolute;left:22px;font-size:14px;color:#222}
.login .field{position:absolute;left:114px;width:207px;height:23px;border:1px solid #c8c8c8;background:#fff}
.login .forgot{position:absolute;left:22px;top:139px;font-size:14px;font-weight:700;color:var(--orange-dark);display:flex;align-items:center;gap:8px}
.login .forgot i{width:8px;height:10px;background:#333;clip-path:polygon(0 0,100% 50%,0 100%)}
.btn-login{position:absolute;left:253px;top:133px;width:75px;height:32px;border-radius:6px;background:linear-gradient(#5cc0f2,var(--sky));color:#fff;font-size:15px;font-weight:700;display:flex;align-items:center;justify-content:center;box-shadow:0 2px 3px rgba(0,0,0,.2)}
.news{left:484px;top:749px;width:347px;height:197px;background:#fff;border:1px solid var(--line);border-radius:8px;overflow:hidden}
.news .tabbar{height:37px;background:#e6e6e6;border-bottom:1px solid #dcdcdc}
.news .tab{position:absolute;left:3px;top:5px;width:159px;height:32px;background:#fff;border-radius:6px 6px 0 0;font-size:12px;font-weight:700;color:#222;display:flex;align-items:center;justify-content:center}
.news ul{list-style:none;position:absolute;left:14px;top:53px}
.news li{display:flex;align-items:center;gap:10px;height:20px;margin-bottom:10.5px;font-size:12.5px;color:#333}
.news li i{width:10px;height:10px;border-radius:50%;background:var(--orange)}
.news .foot{position:absolute;left:0;bottom:0;width:100%;height:30px;border-top:1px solid #ddd;font-size:12px;color:#1b5ea8;text-align:right;padding:9px 14px}
.service-tab{left:884px;top:753px;width:190px;height:26px;background:linear-gradient(#1a8fe0,#0b6fc2);color:#fff;font-size:15px;font-weight:700;padding:4px 13px}
.service-box{left:844px;top:787px;width:199px;height:156px;background:#fff;border:1px solid var(--line);border-radius:6px;overflow:hidden}
.service-box .bar{height:26px;background:#e6e6e6;border-bottom:1px solid #ddd}
.service-box .inner-tab{position:absolute;left:3px;top:4px;width:90px;height:22px;background:#fff}
.service-box .foot{position:absolute;bottom:0;width:100%;height:24px;border-top:1px solid #ddd}
.testimonial{left:137px;top:966px;font-family:'Questrial',sans-serif;font-size:52px;color:#8a8a8a;text-shadow:0 1px 0 #fff}
.brace{left:409px;top:955px;font-family:'Questrial',sans-serif;font-size:90px;color:#9a9a9a;line-height:1}
.quote{left:472px;top:977px;width:570px;font-family:'Lora',serif;font-style:italic;font-size:15.8px;line-height:20.4px;color:#9a9a9a}
.quote-author{left:828px;top:1032px;font-family:'Lora',serif;font-style:italic;font-size:17px;color:#777}
.floor{left:226px;top:1072px;width:612px;height:16px;border-radius:50%;background:radial-gradient(rgba(0,0,0,.18),transparent 70%)}
.footer{left:0;top:1103px;width:1158px;height:97px;background:var(--footer)}
.footer .social{position:absolute;top:34px;width:29px;height:29px;border-radius:5px}
</style>
</head>
<body>
<div class="abs backdrop" role="img" aria-label="Abstract green swoosh background"></div>

<header class="abs header"></header>
<div class="abs brand">
  <span class="brand-mark"></span>
  <span class="brand-name">LEDGER LOOM</span>
</div>
<div class="abs follow">
  <span class="label">Follow us on:</span>
  <span class="item"><span class="dot"></span>Kinfolk</span>
  <span class="item"><span class="dot"></span>Chirper</span>
  <span class="item"><span class="dot" style="background:#f08a1c"></span>RSS</span>
</div>

<div class="abs panel"></div>

<nav class="abs nav">
  <svg style="position:absolute;left:20px;top:12px" width="20" height="20" viewBox="0 0 20 20" aria-hidden="true"><path d="M10 1 L19 10 H16 V19 H12 V13 H8 V19 H4 V10 H1Z" fill="#777"/></svg>
  <a style="left:48px">Home</a><span class="sep" style="left:106px"></span>
  <a style="left:122px">About</a><span class="sep" style="left:184px"></span>
  <a style="left:208px">Services</a><span class="sep" style="left:283px"></span>
  <a style="left:303px">News</a><span class="sep" style="left:370px"></span>
  <a style="left:392px">Contact</a><span class="sep" style="left:466px"></span>
  <a style="left:486px">Portfolio</a><span class="sep" style="left:563px"></span>
</nav>

<div class="abs hero" role="img" aria-label="Banner photograph of large golden currency symbols"></div>

<section class="abs card" style="left:170px">
  <div class="art" role="img" aria-label="Illustration of a businessman with cash" style="background:linear-gradient(#f2a640,#2b2f3a)"></div>
  <h2 style="color:var(--red)">Search for a loan</h2>
  <p>We would like to see a design mockup</p>
  <div class="btn-more">More</div>
</section>
<section class="abs card" style="left:458px">
  <div class="art" role="img" aria-label="Illustration of a hand holding banknotes" style="background:linear-gradient(#cfd8c0,#4f6b3a)"></div>
  <h2 style="color:var(--blue)">Create a payment plan</h2>
  <p>We would like to see a design mockup</p>
  <div class="btn-more">More</div>
</section>
<section class="abs card" style="left:742px">
  <div class="art" role="img" aria-label="Illustration of a stack of banknotes" style="background:linear-gradient(#d9e4cf,#7aa060)"></div>
  <h2 style="color:#111">Make a payment</h2>
  <p>We would like to see a design mockup</p>
  <div class="btn-more">More</div>
</section>

<h1 class="abs welcome">Welcome to our planed finance site!</h1>
<p class="abs intro">Lorem Ipsum availableLorem Ipsum availableLorem Ipsum availableLorem Ipsum availableLorem Ipsum availableLorem Ipsum availableLorem Ipsum availableLorem Ipsum availableLorem Ipsum availableLorem Ipsum availableLorem Ipsum availableLorem Ipsum availableLorem Ipsum available</p>
<div class="abs more-large">More</div>

<div class="abs ribbon" role="img" aria-label="Green ribbon banner"></div>
<div class="abs ribbon-text">Register Now</div>

<section class="abs login">
  <h3>Member login</h3>
  <label style="top:64px">Username :</label><span class="field" style="top:62px"></span>
  <label style="top:99px">Password :</label><span class="field" style="top:97px"></span>
  <span class="forgot"><i></i>Forgot Password?</span>
  <span class="btn-login">Login</span>
</section>

<section class="abs news">
  <div class="tabbar"></div>
  <div class="tab">NEWS &amp; EVENTS</div>
  <ul>
    <li><i></i>Lorem ipsum dolor sit amet, consectetur adipiscing</li>
    <li><i></i>Lorem ipsum dolor sit amet, consectetur adipiscing</li>
    <li><i></i>Lorem ipsum dolor sit amet, consectetur adipiscing</li>
    <li><i></i>Lorem ipsum dolor sit amet, consectetur adipiscing</li>
  </ul>
  <div class="foot">› More</div>
</section>

<div class="abs service-tab">Latest Service</div>
<section class="abs service-box">
  <div class="bar"></div><div class="inner-tab"></div><div class="foot"></div>
</section>

<div class="abs testimonial">Testimonial</div>
<div class="abs brace">{</div>
<p class="abs quote">Lorem ipsum dolor sit amet, consectetur adipiscing elit. Sed ornare, tortor eu aliquam posuere, sem tortor semper urna, nec lacinia nibh nisi vel elit. Phasellus placerat, felis id rhoncus vulputate.</p>
<div class="abs quote-author">MD Name</div>
<div class="abs floor"></div>

<footer class="abs footer">
  <span class="social" style="left:953px;background:#4fa8dc"></span>
  <span class="social" style="left:992px;background:#3b5b9a"></span>
  <span class="social" style="left:1030px;background:#ef8a2a"></span>
</footer>
</body>
</html>
```